Safety Brochure for Industry Assocations

This is an 8.5 x 11 single sided brochure for our Occupational Health and Safety Data Analytics software. If you need to use stock images we will pay for them.

Please incorporate our logo and some of the images. No need to incorporate them all. We like the idea of the boots being at the bottom of the page but we're open to other ideas.

Please note that we intend to mail this brochure to different industries so it should be generic (i.e. not construction specific).

Target Market(s)

Safety and Industry Organisations for construction, mining, forestry and oil and gas industries.

Industry/Entity Type

Industry

Font styles to use
Sans Serif

Colors

Designer to choose colors to be used in the design.

Requirements
Must have
• We are a software company that produces safety software. Our customers are companies that engage in dangerous work and use our software to improve their worker's safety. The look and feel should convey the fact that:
• -We are Big Data
• -We are Software
• -We service industry
Nice to have
• Please see the Pixlore photo of the boots. We were hoping that the desiger would be able ti modify the image with an overlay of 0's and 1's in a kind of "matrix" fashion to indicate that we are merging traditional labour work with software.
Should not have
• No medical symbols. Note that WE ARE NOT HEALTH CARE.

```html
<!DOCTYPE html>
<html lang="en">
<head>
<meta charset="utf-8">
<title>Vantara Analytics – Safety Data Brochure</title>
<link rel="stylesheet" href="https://fonts.googleapis.com/css2?family=Montserrat:wght@400;500;600;700&display=swap">
<style>
  :root {
    --page-bg: #e6e4e1;
    --paper: #ffffff;
    --charcoal: #2e2e30;
    --charcoal-deep: #232325;
    --bar-faint: rgba(255,255,255,0.05);
    --lime: #8dc63f;
    --green: #3fae3f;
    --green-deep: #1f7a2a;
    --matrix-dark: #0d2a14;
    --text-light: #f2f2f2;
    --text-dark: #222222;
  }
  * { box-sizing: border-box; margin: 0; padding: 0; }
  html, body { width: 1200px; height: 993px; overflow: hidden; }
  body {
    background: var(--page-bg);
    font-family: "Montserrat", Arial, sans-serif;
    position: relative;
  }
  .brochure {
    position: absolute;
    left: 237px; top: 26px;
    width: 726px; height: 940px;
    background: var(--paper);
    overflow: hidden;
    box-shadow: 0 6px 18px rgba(0,0,0,0.18);
  }
  .header-tab {
    position: absolute; left: 0; top: 0;
    width: 726px; height: 140px;
  }
  .brand {
    position: absolute; top: 62px; left: 0; width: 100%;
    display: flex; justify-content: center; align-items: center; gap: 12px;
  }
  .brand-mark {
    width: 40px; height: 40px; border-radius: 50%;
    background: var(--green);
  }
  .brand-name {
    font-weight: 600; font-size: 24px; letter-spacing: 2px;
    color: var(--text-dark);
  }
  .hero {
    position: absolute; left: 0; top: 140px;
    width: 726px; height: 350px;
    background: var(--charcoal);
    color: var(--text-light);
    text-align: center;
  }
  .hero-chart { position: absolute; left: 0; bottom: 0; }
  .headline {
    position: relative;
    margin-top: 26px;
    font-weight: 400; font-size: 28px; letter-spacing: 1px;
  }
  .headline-strong {
    display: inline-block;
    font-weight: 700; font-size: 26px; letter-spacing: 1.5px;
    border-bottom: 3px solid var(--lime);
    padding-bottom: 2px; margin-top: 2px;
  }
  .pillars {
    position: relative;
    list-style: none;
    margin-top: 14px;
    font-size: 13.5px; line-height: 20px;
  }
  .pillars strong { font-weight: 700; }
  .section-rule {
    position: absolute; top: 228px; left: 40px; right: 40px;
    display: flex; align-items: center; gap: 16px;
  }
  .section-rule::before, .section-rule::after {
    content: ""; flex: 1; height: 2px; background: var(--text-light);
  }
  .section-title { font-weight: 700; font-size: 22px; }
  .services {
    position: absolute; left: 0; top: 410px; width: 726px;
  }
  .service {
    position: absolute; width: 192px;
    background: var(--green); color: var(--text-light);
    text-align: center;
  }
  .service-title {
    background: var(--lime);
    font-weight: 700; font-size: 16px; letter-spacing: 1px;
    padding: 18px 6px;
  }
  .service-list {
    list-style: none; font-size: 12.5px; line-height: 17px;
    padding: 16px 10px 20px;
  }
  .service-list li { margin-bottom: 12px; }
  .service-list li:last-child { margin-bottom: 0; }
  .service--training { left: 46px; top: 0; height: 180px; }
  .service--benchmark { left: 267px; top: 14px; height: 196px; }
  .service--trend { left: 488px; top: 28px; height: 180px; }
  .field-photo {
    position: absolute; left: 0; top: 625px;
    width: 726px; height: 315px;
    background: linear-gradient(180deg, #1c5a2a 0%, var(--matrix-dark) 55%, #123d1d 100%);
  }
  .tagline {
    position: absolute; left: 0; top: 735px; width: 726px;
    background: rgba(31,122,42,0.85);
    color: #fff; text-align: center;
    font-weight: 700; font-size: 19px; line-height: 24px;
    padding: 10px 0;
  }
  .contact-plate { position: absolute; left: 0; bottom: 0; }
  .contact {
    position: absolute; left: 0; bottom: 24px; width: 726px;
    text-align: center; color: var(--text-dark);
    font-weight: 700; font-size: 14px; line-height: 20px;
  }
</style>
</head>
<body>
  <main class="brochure">
    <svg class="header-tab" viewBox="0 0 726 140" aria-hidden="true">
      <polygon points="150,0 726,0 726,140 0,140 0,120 700,120 700,50 175,50" fill="var(--charcoal)"/>
      <rect x="0" y="50" width="726" height="70" fill="var(--paper)"/>
      <polygon points="150,30 726,30 726,52 175,52" fill="var(--charcoal-deep)"/>
    </svg>

    <div class="brand">
      <span class="brand-mark"></span>
      <span class="brand-name">Vantara Analytics</span>
    </div>

    <section class="hero">
      <svg class="hero-chart" width="726" height="300" viewBox="0 0 726 300" aria-hidden="true">
        <g fill="var(--bar-faint)">
          <rect x="30" y="170" width="22" height="130"/>
          <rect x="60" y="120" width="22" height="180"/>
          <rect x="90" y="150" width="22" height="150"/>
          <rect x="120" y="100" width="22" height="200"/>
          <rect x="590" y="140" width="22" height="160"/>
          <rect x="620" y="90" width="22" height="210"/>
          <rect x="650" y="130" width="22" height="170"/>
          <rect x="680" y="70" width="22" height="230"/>
        </g>
      </svg>
      <h1 class="headline">LEVERAGE THE POWER OF<br><span class="headline-strong">BIG DATA!</span></h1>
      <ul class="pillars">
        <li><strong>LEAD</strong> the next wave of injury reduction</li>
        <li><strong>ENGAGE</strong> with members through collaboration and benchmarking</li>
        <li><strong>PROMOTE</strong> standardization</li>
        <li><strong>ANALYZE</strong> Accurate, Timely and Complete Leading Indicators</li>
        <li><strong>TRAIN</strong> industry more proactively</li>
      </ul>
      <div class="section-rule"><h2 class="section-title">EHS Data</h2></div>
    </section>

    <section class="services">
      <article class="service service--training">
        <h3 class="service-title">TRAINING</h3>
        <ul class="service-list">
          <li>Analyze needs of Industry</li>
          <li>Deliver Proactive Training</li>
          <li>Improve Safety</li>
        </ul>
      </article>
      <article class="service service--benchmark">
        <h3 class="service-title">BENCHMARKING</h3>
        <ul class="service-list">
          <li>Engage with Members</li>
          <li>Promote Collaborative Advancement of Safety</li>
          <li>Improve Safety</li>
        </ul>
      </article>
      <article class="service service--trend">
        <h3 class="service-title">TREND ANALYSIS</h3>
        <ul class="service-list">
          <li>Monitor Industry Trends</li>
          <li>Implement Corrective Initiatives</li>
          <li>Improve Safety</li>
        </ul>
      </article>
    </section>

    <div class="field-photo" role="img" aria-label="Worn work boots on the ground overlaid with a green matrix of falling binary digits"></div>

    <p class="tagline">The next BIG STEP in injury reduction<br>For your entire industry</p>

    <svg class="contact-plate" width="726" height="90" viewBox="0 0 726 90" aria-hidden="true">
      <polygon points="175,0 560,0 590,90 145,90" fill="var(--paper)"/>
    </svg>
    <address class="contact" style="font-style:normal">
      1-888-555-0142<br>www.vantaradata.com
    </address>
  </main>
</body>
</html>
```